Business card and Stationery for data intelligence company

We need a new design for our business cards and stationery (Business Letter templates and a Quote example on Word, but it MUST work on Google Doc as well).

We are a software company based in Ireland and UK. Our product is "Kovar", data intelligence platform with beautiful visualizations, graph capabilities (things are interconnected), powerful, flexible, it can manage Big Data and Streaming information. It's modern and relatively open source.
Our company will provide data intelligence for law enforcements, pharmaceuticals, and similar high end customers.

We'll launch a new website soon. At the moment it's http://www.kovar-analytics.example if you want to take a look. This is our youtube channel in case you need it to understand what Kovar is: https://www.youtube.com/c/kovaranalyticschannel

We changed the logo so please use the logo I attach here.

We'd like the output to be cool and modern but elegant and "business" at the same time. It should inspire simple sophistication, "unity" "intent" "purpose" yet subtly very advanced and innovative.

The name "Kovar" does NOT refer to sirens (mithological creatures) as well as the warning devices. It means Kinetic Object Vector Analysis Reactor. Please use our logo's colors and if you want to something like the "graph" image.

```html
<!DOCTYPE html>
<html lang="en">
<head>
<meta charset="utf-8">
<title>Kovar business card</title>
<link href="https://fonts.googleapis.com/css2?family=Roboto:wght@400;500&family=Montserrat:wght@500&display=swap" rel="stylesheet">
<style>
  :root {
    --backdrop: #3a3a3a;
    --paper: #f3f3f2;
    --orange: #f2a531;
    --grey: #a9a9a9;
    --ink: #222222;
    --photo-tone: #b8b8b8;
  }
  * { box-sizing: border-box; margin: 0; padding: 0; }
  html, body { width: 1200px; height: 1032px; overflow: hidden; }
  body {
    background: var(--backdrop);
    font-family: "Roboto", Arial, sans-serif;
    position: relative;
  }
  .card {
    position: absolute;
    left: 250px;
    width: 700px;
    height: 400px;
    background: var(--paper);
    overflow: hidden;
    box-shadow: 0 14px 30px rgba(0,0,0,.45);
  }
  .card--front { top: 96px; }
  .card--back { top: 536px; }

  /* front */
  .portrait {
    position: absolute;
    left: 110px; top: 90px;
    width: 160px; height: 160px;
    border-radius: 50%;
    border: 6px solid var(--orange);
    background: radial-gradient(circle at 50% 40%, #d4d4d4, var(--photo-tone) 60%, #7d7d7d);
    z-index: 2;
  }
  .identity { position: absolute; left: 300px; top: 110px; z-index: 2; }
  .identity__name { color: var(--orange); font-size: 30px; font-weight: 500; }
  .identity__role { color: var(--ink); font-size: 15px; margin-top: 6px; text-transform: uppercase; }

  .contact {
    position: absolute;
    bottom: 0;
    display: flex; flex-direction: column; align-items: center; justify-content: center;
    gap: 8px;
    padding: 0 8px;
    color: var(--ink);
    font-size: 15px;
    text-align: center;
    white-space: nowrap;
  }
  .contact svg { width: 26px; height: 26px; fill: var(--ink); }
  .contact--phone { left: 0; width: 260px; height: 110px; background: var(--grey); }
  .contact--mail { left: 260px; width: 230px; height: 140px; background: var(--orange); font-size: 14px; }
  .contact--web {
    left: 490px; width: 210px; height: 190px;
    background: var(--grey);
    font-size: 13px;
    justify-content: flex-start;
    padding-top: 34px;
  }

  /* back */
  .brand {
    position: absolute;
    left: 0; right: 0; top: 120px;
    display: flex; align-items: center; justify-content: center; gap: 26px;
  }
  .brand__dot { width: 90px; height: 90px; border-radius: 50%; border: 14px solid var(--orange); }
  .brand__name {
    font-family: "Montserrat", Arial, sans-serif;
    font-weight: 500;
    font-size: 96px;
    letter-spacing: 14px;
    color: var(--orange);
  }
  .stripe { position: absolute; bottom: 0; }
  .stripe--left { left: 0; width: 300px; height: 34px; background: var(--orange); }
  .stripe--mid { left: 300px; width: 200px; height: 50px; background: var(--grey); }
  .stripe--right { left: 500px; width: 200px; height: 70px; background: var(--orange); }
</style>
</head>
<body>
  <section class="card card--front">
    <div class="portrait" role="img" aria-label="Portrait photograph of the card holder"></div>
    <div class="identity">
      <p class="identity__name">Marco Bellandi</p>
      <p class="identity__role">CEO Kovar Solutions</p>
    </div>
    <div class="contact contact--phone">
      <svg viewBox="0 0 24 24" aria-hidden="true"><path d="M6.6 10.8a15 15 0 0 0 6.6 6.6l2.2-2.2c.3-.3.7-.4 1-.2 1.1.4 2.3.6 3.6.6.6 0 1 .4 1 1V20c0 .6-.4 1-1 1A17 17 0 0 1 3 4c0-.6.4-1 1-1h3.5c.6 0 1 .4 1 1 0 1.3.2 2.5.6 3.6.1.3 0 .7-.2 1z"/></svg>
      <span>+353 87 555 0142</span>
    </div>
    <div class="contact contact--mail">
      <svg viewBox="0 0 24 24" aria-hidden="true"><path d="M2 5h20v14H2z" fill="var(--ink)"/><path d="M2 5l10 8 10-8" fill="none" stroke="var(--orange)" stroke-width="1.6"/></svg>
      <span>info@kovar-analytics.example</span>
    </div>
    <div class="contact contact--web">
      <svg viewBox="0 0 24 24" aria-hidden="true"><circle cx="12" cy="12" r="9" fill="none" stroke="var(--ink)" stroke-width="1.8"/><ellipse cx="12" cy="12" rx="4" ry="9" fill="none" stroke="var(--ink)" stroke-width="1.6"/><path d="M3 12h18M5 7h14M5 17h14" stroke="var(--ink)" stroke-width="1.4"/></svg>
      <span>www.kovar-analytics.example</span>
    </div>
  </section>

  <section class="card card--back">
    <div class="brand">
      <span class="brand__dot"></span>
      <span class="brand__name">KOVAR</span>
    </div>
    <span class="stripe stripe--left"></span>
    <span class="stripe stripe--mid"></span>
    <span class="stripe stripe--right"></span>
  </section>
</body>
</html>
```